Turn Photo into Graphic Design Image for Home Page

We need to take a photo and create a graphic image for our home page. We are currently using a monochrome (green) cut out version of the attached photo. (see www.belvintorlegal.example) We are creating a new website, but would like to use the same photo, but with a background (either texture, or a skyline of Austin). I am open to manipulating the photo and background in any way you want to try (although don't keep the current background). It doesn't have to be green, although that is our current branding. It doesn't have to be monochrome either. Basically, I'd like to see what you come up with. I'd like to design to be cool/edgy. It can be minimal. It needs to be modern. It needs to be the dimensions of a webpage (rectangular). With the person (me) on the right hand side. In the same position as the belvintorlegal.example page.

Requirements
Should not have
• The image should not have any text on it.

```html
<!DOCTYPE html>
<html lang="en">
<head>
<meta charset="utf-8">
<title>The Law Office of Belvin Tor</title>
<link href="https://fonts.googleapis.com/css2?family=Lato:ital,wght@0,300;0,400;0,700;0,900;1,400;1,700&display=swap" rel="stylesheet">
<style>
  :root {
    --sky-top: #efe9e6;
    --sky-blush: #e4d3d6;
    --haze: #cfc6da;
    --city-mist: #b9b4cc;
    --city-warm: #c9b4b8;
    --city-low: #a7a5bf;
    --ledge: #6e5648;
    --ledge-dark: #3a2d26;
    --white: #ffffff;
    --nav-text: #f7f3f7;
    --brand-green: #1f6b2a;
    --icon-tint: #a79bbd;
  }
  * { margin: 0; padding: 0; box-sizing: border-box; }
  html, body { width: 1200px; height: 589px; overflow: hidden; }
  body { font-family: 'Lato', sans-serif; position: relative; background: var(--sky-top); }

  .hero-backdrop {
    position: absolute; inset: 0;
    background:
      radial-gradient(ellipse 420px 120px at 300px 330px, rgba(150,130,150,0.35), transparent 70%),
      radial-gradient(ellipse 300px 160px at 560px 420px, rgba(190,150,150,0.35), transparent 70%),
      radial-gradient(ellipse 260px 110px at 120px 470px, rgba(200,170,160,0.35), transparent 70%),
      radial-gradient(ellipse 380px 130px at 1080px 470px, rgba(170,150,170,0.35), transparent 70%),
      linear-gradient(180deg, var(--sky-top) 0%, var(--sky-blush) 22%, var(--haze) 42%, var(--city-mist) 58%, var(--city-warm) 75%, var(--city-low) 100%);
  }
  .attorney-portrait {
    position: absolute; left: 742px; top: 91px; width: 222px; height: 498px;
    background: linear-gradient(180deg, #a98672 0%, #b08d78 16%, #8f8f90 24%, #8a9fbf 34%, #8c8c8b 55%, #7e7d7b 80%, #4d4440 100%);
    border-radius: 48px 48px 8px 8px;
    opacity: 0.85;
  }
  .stone-ledge {
    position: absolute; left: 0; bottom: 0; width: 1200px; height: 40px;
    background: linear-gradient(180deg, var(--ledge) 0%, var(--ledge-dark) 100%);
  }

  .site-nav {
    position: absolute; left: 122px; top: 46px;
    display: flex; align-items: center;
    font-size: 16px; color: var(--nav-text);
  }
  .site-nav a { color: inherit; text-decoration: none; }
  .site-nav a.is-current { color: var(--brand-green); font-weight: 700; }
  .site-nav .divider { margin: 0 9px; font-size: 12px; opacity: 0.8; }

  .contact-box {
    position: absolute; left: 951px; top: 38px;
    font-size: 13px; font-weight: 900; line-height: 20px;
  }
  .contact-row { display: flex; align-items: center; gap: 7px; }
  .contact-row svg { width: 14px; height: 14px; }
  .phone-number { color: var(--brand-green); }
  .pay-online { color: var(--white); letter-spacing: 0.3px; }

  .title-block { position: absolute; left: 122px; top: 183px; display: inline-block; color: var(--white); }
  .title-kicker { font-weight: 300; font-size: 33px; letter-spacing: -0.5px; line-height: 36px; }
  .title-name { font-weight: 900; font-size: 60px; line-height: 64px; letter-spacing: -1px; }
  .title-city { text-align: right; font-style: italic; font-weight: 700; font-size: 12px; margin-top: 2px; }

  .practice-prompt {
    position: absolute; left: 122px; top: 391px;
    font-style: italic; font-weight: 700; font-size: 11px; color: var(--white);
  }
  .practice-areas { position: absolute; left: 0; top: 429px; width: 700px; height: 120px; }
  .practice-item {
    position: absolute; width: 100px; margin-left: -50px;
    display: flex; flex-direction: column; align-items: center;
    color: var(--white); font-size: 12px; font-weight: 700; text-align: center; line-height: 15px;
  }
  .practice-icon {
    width: 60px; height: 60px; border-radius: 50%; background: var(--white);
    display: flex; align-items: center; justify-content: center; margin-bottom: 12px;
  }
  .practice-icon svg { width: 36px; height: 36px; fill: var(--icon-tint); }
</style>
</head>
<body>
  <div class="hero-backdrop" role="img" aria-label="Hazy pastel photograph of a city skyline at dusk"></div>
  <div class="attorney-portrait" role="img" aria-label="Photograph of the attorney in a grey suit holding a briefcase"></div>
  <div class="stone-ledge" role="img" aria-label="Rough stone ledge in the foreground"></div>

  <nav class="site-nav">
    <a class="is-current" href="#">Home</a><span class="divider">|</span>
    <a href="#">Areas of Practice</a><span class="divider">|</span>
    <a href="#">About</a><span class="divider">|</span>
    <a href="#">FAQ</a><span class="divider">|</span>
    <a href="#">Reviews</a><span class="divider">|</span>
    <a href="#">Videos</a><span class="divider">|</span>
    <a href="#">DWI eBook</a><span class="divider">|</span>
    <a href="#">Contact</a>
  </nav>

  <div class="contact-box">
    <div class="contact-row">
      <svg viewBox="0 0 14 14"><rect width="14" height="14" rx="2" fill="#fff"/><path d="M4 3l2 0 1 2.5-1.2 1a6 6 0 0 0 2.7 2.7l1-1.2 2.5 1 0 2a1 1 0 0 1-1 1A8 8 0 0 1 3 4a1 1 0 0 1 1-1z" fill="#d8cfdf"/></svg>
      <span class="phone-number">(512) 555-0148</span>
    </div>
    <div class="contact-row">
      <svg viewBox="0 0 14 14"><rect width="14" height="14" rx="2" fill="#fff"/><text x="7" y="11" font-size="10" font-weight="900" text-anchor="middle" fill="#d8cfdf" font-family="Lato, sans-serif">$</text></svg>
      <span class="pay-online">PAY ONLINE</span>
    </div>
  </div>

  <header class="title-block">
    <div class="title-kicker">THE LAW OFFICE OF</div>
    <h1 class="title-name">BELVIN TOR</h1>
    <div class="title-city">Austin, TX</div>
  </header>

  <p class="practice-prompt">Please select your area of interest</p>

  <div class="practice-areas">
    <div class="practice-item" style="left:155px">
      <div class="practice-icon"><svg viewBox="0 0 36 36"><path d="M8 16l3-7h14l3 7h2v10h-4v3h-4v-3H13v3H9v-3H5V16z"/></svg></div>DWI
    </div>
    <div class="practice-item" style="left:246px">
      <div class="practice-icon"><svg viewBox="0 0 36 36"><path d="M9 16h18v14H9z"/><path d="M12 16v-5a6 6 0 0 1 12 0" fill="none" stroke="#a79bbd" stroke-width="3"/></svg></div>Theft
    </div>
    <div class="practice-item" style="left:341px">
      <div class="practice-icon"><svg viewBox="0 0 36 36"><circle cx="18" cy="14" r="7"/><path d="M6 18c6 0 11 4 12 12C11 30 6 25 6 18zM30 18c-6 0-11 4-12 12 7 0 12-5 12-12z"/></svg></div>Marijuana /<br>Drugs
    </div>
    <div class="practice-item" style="left:437px">
      <div class="practice-icon"><svg viewBox="0 0 36 36"><circle cx="10" cy="20" r="6" fill="none" stroke="#a79bbd" stroke-width="3"/><circle cx="26" cy="20" r="6" fill="none" stroke="#a79bbd" stroke-width="3"/><path d="M15 15h6v3h-6z"/></svg></div>Assault
    </div>
    <div class="practice-item" style="left:533px">
      <div class="practice-icon"><svg viewBox="0 0 36 36"><path d="M9 6h18v26H9z"/><path d="M14 4h8v5h-8z"/><path d="M12 13h12M12 17h12M12 21h12M12 25h12" stroke="#fff" stroke-width="1.6"/></svg></div>Warrants &amp; Jail<br>Release
    </div>
    <div class="practice-item" style="left:630px">
      <div class="practice-icon"><svg viewBox="0 0 36 36"><circle cx="18" cy="18" r="13" fill="none" stroke="#a79bbd" stroke-width="6"/><path d="M9 9l5 5M27 9l-5 5M9 27l5-5M27 27l-5-5" stroke="#fff" stroke-width="3"/></svg></div>Other<br>Misdemeanors<br>or Felonies
    </div>
  </div>
</body>
</html>
```